International Trading Company, 'KIRO' needs a Business Card

The company name is "KIRO" and it has own logo design.
I'd like to use its logo on this business card.
I need two side Business Card.
I'll look forward to your great design.
Thank you very much in advance.

Contact Information for Business Card

Company Name : Kiro Harbour Limited
Information Example
Dorian Pallister
Mobile(use icon please) : 1 (212) 555-0143
Tel(use icon please) : 1 (212) 555-0178
Email(use icon please) : dorian27@kiroharbour-mail.com
Address(use icon please) : 482 Halden Ave, New York, NY 10160, USA

```html
<!DOCTYPE html>
<html lang="en">
<head>
<meta charset="utf-8">
<title>Kiro Harbour Limited — Business Card</title>
<link rel="stylesheet" href="https://fonts.googleapis.com/css2?family=Roboto:wght@400;500;700&family=Roboto+Condensed:wght@500&display=swap">
<style>
  :root {
    --backdrop: #d9d9d9;
    --card-light: #f2f2f2;
    --card-dark: #555556;
    --ink: #555556;
    --ink-soft: #717171;
    --rule: #8a8a8a;
    --stripe: #a3a3a3;
    --paper-text: #f4f4f4;
  }
  * { margin: 0; padding: 0; box-sizing: border-box; }
  html, body {
    width: 1200px; height: 960px; overflow: hidden;
    background: var(--backdrop);
    font-family: "Roboto", Arial, sans-serif;
  }
  .canvas { position: relative; width: 1200px; height: 960px; }

  .card {
    position: absolute;
    width: 600px; height: 344px;
    box-shadow: 0 2px 4px rgba(0,0,0,0.25);
    overflow: hidden;
  }
  .card--front { left: 314px; top: 113px; background: var(--card-light); color: var(--ink); }
  .card--back { left: 311px; top: 472px; background: var(--card-dark); color: var(--paper-text); }

  .wordmark {
    position: absolute;
    font-family: "Roboto", Arial, sans-serif;
    font-weight: 700;
    line-height: 1;
    letter-spacing: 1px;
  }
  .card--front .wordmark { right: 34px; top: 38px; font-size: 73px; color: var(--ink); }
  .card--back .wordmark { left: 0; right: 0; top: 128px; text-align: center; font-size: 94px; color: var(--paper-text); }

  .holder { position: absolute; left: 34px; top: 163px; }
  .holder__name {
    font-family: "Roboto Condensed", "Arial Narrow", sans-serif;
    font-weight: 500; font-size: 22px; color: var(--ink); line-height: 1;
  }
  .holder__role { font-size: 14.5px; color: var(--ink-soft); margin-top: 7px; line-height: 1; }

  .divider {
    position: absolute; left: 34px; top: 218px; width: 531px; height: 1px; background: var(--rule);
  }

  .contact { position: absolute; left: 34px; top: 232px; list-style: none; }
  .contact li {
    display: flex; align-items: center; gap: 7px;
    font-size: 14.5px; line-height: 19.5px; color: var(--ink);
  }
  .contact svg { width: 14px; height: 14px; fill: var(--ink); flex: none; }

  .address {
    position: absolute; right: 34px; top: 233px;
    font-style: normal; text-align: right;
    font-size: 14.5px; line-height: 18.5px; color: var(--ink);
  }

  .footer-band { position: absolute; left: 0; bottom: 0; width: 600px; height: 40px; }
  .footer-band__url {
    position: absolute; right: 28px; bottom: 12px;
    font-size: 14px; letter-spacing: 1.6px; color: var(--paper-text);
  }

  .card--back .site-url {
    position: absolute; left: 0; right: 0; top: 287px; text-align: center;
    font-size: 14.5px; letter-spacing: 4.2px; color: var(--paper-text);
  }
</style>
</head>
<body>
<main class="canvas">

  <section class="card card--front" aria-label="Business card front">
    <div class="wordmark">KIRO</div>

    <div class="holder">
      <div class="holder__name">DORIAN PALLISTER</div>
      <div class="holder__role">CEO/FOUNDER</div>
    </div>

    <div class="divider"></div>

    <ul class="contact">
      <li>
        <svg viewBox="0 0 24 24" aria-hidden="true"><path d="M6.6 10.8a15.1 15.1 0 0 0 6.6 6.6l2.2-2.2c.3-.3.7-.4 1-.2 1.1.4 2.3.6 3.6.6.6 0 1 .4 1 1V20c0 .6-.4 1-1 1A17 17 0 0 1 3 4c0-.6.4-1 1-1h3.5c.6 0 1 .4 1 1 0 1.3.2 2.5.6 3.6.1.3 0 .7-.2 1z"/></svg>
        1 (212) 555-0178
      </li>
      <li>
        <svg viewBox="0 0 24 24" aria-hidden="true"><path d="M7 1h10a2 2 0 0 1 2 2v18a2 2 0 0 1-2 2H7a2 2 0 0 1-2-2V3a2 2 0 0 1 2-2zm0 3v14h10V4zm5 15.2a1.2 1.2 0 1 0 0 2.4 1.2 1.2 0 0 0 0-2.4z"/></svg>
        1 (212) 555-0143
      </li>
      <li>
        <svg viewBox="0 0 24 24" aria-hidden="true"><path d="M2 5h20v2.2l-10 6-10-6zm0 4.6 10 6 10-6V19H2z"/></svg>
        dorian27@kiroharbour-mail.com
      </li>
    </ul>

    <address class="address">
      482 Halden Ave<br>
      New York<br>
      NY 10160, USA
    </address>

    <div class="footer-band">
      <svg width="600" height="40" viewBox="0 0 600 40" aria-hidden="true">
        <polygon points="0,15 346,15 338,24 0,24" fill="var(--stripe)"/>
        <polygon points="0,26 336,26 351,1 600,1 600,40 0,40" fill="var(--card-dark)"/>
      </svg>
      <span class="footer-band__url">www.kiroharbour.com</span>
    </div>
  </section>

  <section class="card card--back" aria-label="Business card back">
    <div class="wordmark">KIRO</div>
    <div class="site-url">www.kiroharbour.com</div>
  </section>

</main>
</body>
</html>
```